Bathroom, Plumbing & TIling Business

I require a business card design for me new business the 'Ashgrove Tileworks Studio', based in Melbourne, Victoria.

Specialising in bathroom refurbishments, new installations, repairs, plumbing and tiling, the Ashgrove Tileworks Studio provides a professional high-quality standard of workmanship, creating your dream.

With over 15 years’ experience in the bathroom and plumbing industry the ATS will only take payment once the job is completed to the customers’ satisfaction*. We pride ourselves on hard-work, professionalism, customer service and always delivering that high end finish you have only dreamt of.

The majority of our work, to date, has come through personal recommendation and word-of-mouth and as a family-run company we do not pressure sell or push our customers to have unnecessary works.

The Ashgrove Tileworks Studio can source products for our customers at trade price and will always quote a job realistically, and honestly, on the work and materials required. We always let the customer know how long the job will take and we will complete it within the specified time.

ATS are dedicated to fitting new bathrooms, renovations, waterproofing, shower repairs/leaks and tiling to removing and refitting bathrooms, ensuites and showers and installing plumbing systems.

The business cards for ATS need to be clean, modern and simple. White matt finish with embossed bath logo.

On side 1 of the card we require the words 'Ashgrove Tileworks Studio' to be written in the Anson font with the letter V,B and C a lot larger in size to the other letters. The letter 'y' (at the end of the word 'Company') is to follow under the title in a curved bath shape growing up and around the letter V to a shower head dripping water in to the letter 'V' which will be half filled with water. The colour for the main title is the green colour which is used in the Waterfall colour scheme on MS Publisher. The tag line, 'Creating your Dream', is to be situated in a smaller font size, underneath the main title in the Anson font and be written in black (we think).

Side 2 of the card is to have a smaller sized version of the Side 1 logo (but only saying ATS - not the full title, Ashgrove Tileworks Studio) situated at the top and contact details (again, in the Anson font underneath.

The final design should communicate high-end, high quality and professionalism of bathroom fitting and plumbing works.
Updates

Hi there

Please could you include/list some of the services, provided by ATS on the back of the card:

Bathroom Renovations

Bathroom Installations

Tiling

Shower Repairs

Plumbing

Cheers :-)

Target Market(s)

Home owners, renters, property developers, rental companies seeking anything works related to bathrooms, plumbing and tiling. Age range from 21-70.

Industry/Entity Type

Industry

Requirements
Must have
• Double sided business card
Side 1: main - title (Ashgrove Tileworks Studio), logo (bath & shower) and tag line (Creating your Dream)
Side 2: Smaller sized version of Side 1 (but only with the letters ATS - not the whole company name) and contact details:

Rowan Pelliser (Owner)
Kellbrook, 3188

Website: www.ashgrovetileworksstudio.example
Email: Rowan@ats.example
Phone: +61 491 570 156
Nice to have
• The business cards for ATS need to be clean, modern and simple. White/or off white matt finish with embossed bath logo.

Should not have
• We do not want to see any of the following on the card:

No garish colours
No clip art
No cartoon images of people, baths or plumbing tools
No small photographs of bathrooms or other 'photographic' images

```html
<!DOCTYPE html>
<html lang="en">
<head>
<meta charset="utf-8">
<title>Ashgrove Tileworks Studio – Business Cards</title>
<link rel="stylesheet" href="https://fonts.googleapis.com/css2?family=Poiret+One&display=swap">
<style>
  :root {
    --teal: #179a94;
    --band: #0f9891;
    --ink: #1d1d1d;
    --paper: #ffffff;
    --page: #ffffff;
    --edge: #e6e6e6;
  }
  * { box-sizing: border-box; margin: 0; padding: 0; }
  html, body {
    width: 1200px;
    height: 679px;
    overflow: hidden;
    background: var(--page);
  }
  body {
    position: relative;
    font-family: "Poiret One", sans-serif;
    color: var(--ink);
  }
  .card {
    position: absolute;
    width: 555px;
    height: 307px;
    background: var(--paper);
    border: 1px solid var(--edge);
    box-shadow: 0 4px 14px rgba(0,0,0,0.10);
    overflow: hidden;
    text-align: center;
  }
  .card--front-plain  { left: 28px;  top: 12px; }
  .card--back-plain   { left: 622px; top: 12px; }
  .card--front-band   { left: 28px;  top: 370px; }
  .card--back-band    { left: 622px; top: 370px; }

  .band {
    position: absolute;
    left: 0; right: 0; bottom: 0;
    height: 133px;
    background: var(--band);
    color: var(--paper);
  }

  .wordmark {
    position: absolute;
    left: 0; right: 0;
    display: flex;
    align-items: center;
    justify-content: center;
    gap: 12px;
    color: var(--teal);
    font-weight: 400;
    white-space: nowrap;
  }
  .wordmark__dot {
    width: 14px; height: 14px;
    border: 1.5px solid var(--teal);
    border-radius: 50%;
    flex: none;
  }
  .wordmark--full { top: 82px; font-size: 38px; }
  .wordmark--short { top: 28px; font-size: 44px; letter-spacing: 2px; }

  .tagline {
    position: absolute;
    left: 0; right: 0;
    font-size: 24px;
  }
  .card--front-plain .tagline { top: 190px; color: var(--ink); }
  .band .tagline { top: 47px; color: var(--paper); }

  .contact {
    position: absolute;
    left: 0; right: 0;
    font-size: 19px;
    line-height: 26px;
  }
  .contact__name { font-size: 21px; }
  .card--back-plain .contact--person { top: 108px; }
  .rule {
    position: absolute;
    left: 86px; right: 76px;
    top: 167px;
    height: 1.5px;
    background: var(--teal);
  }
  .card--back-plain .contact--details { top: 174px; }

  .card--back-band .contact--person { top: 117px; }
  .band .contact--details { top: 12px; color: var(--paper); line-height: 26.5px; }

  .phone-icon {
    display: inline-block;
    width: 15px; height: 15px;
    vertical-align: -1px;
    margin-right: 4px;
  }
</style>
</head>
<body>

  <section class="card card--front-plain" aria-label="Front of card, white">
    <div class="wordmark wordmark--full"><span class="wordmark__dot"></span>Ashgrove Tileworks Studio</div>
    <p class="tagline">Creating your Dream</p>
  </section>

  <section class="card card--back-plain" aria-label="Back of card, white">
    <div class="wordmark wordmark--short"><span class="wordmark__dot"></span>ATS</div>
    <div class="contact contact--person">
      <p class="contact__name">Rowan Pelliser</p>
      <p>Kellbrook, 3188</p>
    </div>
    <div class="rule"></div>
    <div class="contact contact--details">
      <p>www.ashgrovetileworksstudio.example</p>
      <p>Email: Rowan@ats.example</p>
      <p>Phone: +61 491 570 156</p>
    </div>
  </section>

  <section class="card card--front-band" aria-label="Front of card, teal band">
    <div class="wordmark wordmark--full"><span class="wordmark__dot"></span>Ashgrove Tileworks Studio</div>
    <div class="band">
      <p class="tagline">Creating your Dream</p>
    </div>
  </section>

  <section class="card card--back-band" aria-label="Back of card, teal band">
    <div class="wordmark wordmark--short"><span class="wordmark__dot"></span>ATS</div>
    <div class="contact contact--person">
      <p class="contact__name">Rowan Pelliser (Owner)</p>
    </div>
    <div class="band">
      <div class="contact contact--details">
        <p>Kellbrook, 3188</p>
        <p>Email: Rowan@ats.example</p>
        <p><svg class="phone-icon" viewBox="0 0 24 24" aria-hidden="true"><path fill="#ffffff" d="M6.6 10.8c1.4 2.8 3.8 5.1 6.6 6.6l2.2-2.2c.3-.3.7-.4 1-.2 1.1.4 2.3.6 3.6.6.6 0 1 .4 1 1V20c0 .6-.4 1-1 1C10.6 21 3 13.4 3 4c0-.6.4-1 1-1h3.5c.6 0 1 .4 1 1 0 1.3.2 2.5.6 3.6.1.3 0 .7-.2 1z"/></svg>+ 61 491 570 156</p>
        <p>www.ashgrovetileworksstudio.example</p>
      </div>
    </div>
  </section>

</body>
</html>
```